On-the-go, individually packaged flushable wipe packaging

Design the front and back of an individually packaged flushable wipe product.

The package is 4 inches tall and 2 inches wide. There are only two sides to the package, front and back. It is constructed of two sheets of printed, foil-lined plastic that are heat welded together.

The front should be decorative and playful and have space for a logo / product name on it (no logo has been created yet so use your imagination if you wish). It should be unisex and envoke somewhat outdoorsy vibes that would appeal to mountain bikers, marathon runners, travelers, and adventurers of all kinds. It can draw attention to itself through color but not through potty humor or bathroom references. People should be able to take these to work or send them with their children to school with being embarrassed.

Important note: Similar to business cards, the packaging material is printed and then cut in a grid. The machine that cuts the packaging may be off by a couple millimeters so any artwork or colors that extend to the sides of the packaging should continue onto the opposite side of the next package like a tesselation or book-matched wood, left side should match up to right side and top should match up to bottom.

The back should contain the follow information (iconography and layout up to you):

- Contains one hygienic towelette
- (Key selling points)
- Flushable & Biodegradable
- 100% natural fibers
- Gentle cleansing formula
- No parabens or fragrances
- (For use on…)
- Hands
- Face*
- Body
- Nether areas
- Messy surfaces
- *Avoid eyes/forehead before sweating and scruff (snags fibers)
- Please care for our planet, cities, and sewer systems by recycling this packaging after use. Do not flush packaging.

```html
<!DOCTYPE html>
<html lang="en">
<head>
<meta charset="utf-8">
<title>Roamfresh Flushable Wipe – Front and Back</title>
<link rel="stylesheet" href="https://fonts.googleapis.com/css2?family=Outfit:wght@400;500;600;800&family=Source+Sans+3:wght@400&family=Oswald:wght@700&display=swap">
<style>
  :root {
    --pack-blue: #1a78c2;
    --seal-blue: #1466a6;
    --seal-grey: #dcdcdc;
    --brand-blue: #1c7cc6;
    --ink-white: #ffffff;
    --icon-line: #1a5fa8;
    --icon-fill: #9fd0ef;
    --box-line: rgba(255,255,255,0.55);
    --page: #ffffff;
  }
  * { box-sizing: border-box; margin: 0; padding: 0; }
  html, body { width: 1200px; height: 952px; overflow: hidden; background: var(--page); }
  .canvas { position: relative; width: 1200px; height: 952px; }

  .pack { position: absolute; background: var(--pack-blue); color: var(--ink-white); font-family: "Outfit", sans-serif; }
  .pack--front { left: 181px; top: 74px; width: 405px; height: 807px; }
  .pack--back  { left: 648px; top: 76px; width: 403px; height: 804px; }

  .seal { position: absolute; left: 0; width: 100%; height: 40px; background: var(--seal-blue); }
  .seal--top { top: 0; }
  .seal--bottom { bottom: 0; }
  .seal__band { position: absolute; top: 0; height: 100%; background: var(--seal-grey); }
  .seal--top .seal__band { left: 70px; width: 265px; }
  .seal--bottom .seal__band { left: 64px; width: 278px; }

  .label-panel { position: absolute; left: 70px; top: 40px; width: 265px; height: 334px; }
  .label-panel svg { display: block; }
  .brand-name {
    position: absolute; left: 70px; top: 195px; width: 265px;
    text-align: center; font-family: "Outfit", sans-serif; font-weight: 800;
    font-size: 62px; line-height: 62px; color: var(--brand-blue); letter-spacing: -1px;
  }

  .product-name {
    position: absolute; left: 0; top: 382px; width: 100%;
    text-align: center; font-family: "Source Sans 3", sans-serif; font-size: 34px; font-weight: 400;
  }

  .benefit { position: absolute; left: 89px; display: flex; align-items: center; }
  .benefit__icon { width: 74px; height: 74px; border-radius: 50%; background: var(--ink-white); display: flex; align-items: center; justify-content: center; }
  .benefit__text { margin-left: 19px; font-size: 15px; font-weight: 500; letter-spacing: 1.2px; line-height: 18.5px; text-transform: uppercase; }
  .benefit--formula { top: 451px; }
  .benefit--fibers { top: 540px; }
  .benefit--free { top: 629px; }

  .use-box { position: absolute; left: 55px; top: 145px; width: 292px; height: 229px; border: 1.5px solid var(--box-line); border-radius: 8px; }
  .use-box__title { position: absolute; top: 25px; width: 100%; text-align: center; font-weight: 600; font-size: 20px; letter-spacing: 0.5px; }
  .use-list { position: absolute; list-style: none; font-weight: 600; font-size: 20px; line-height: 20px; letter-spacing: 0.3px; }
  .use-list li { position: absolute; white-space: nowrap; padding-left: 24px; }
  .use-list li svg { position: absolute; left: 0; top: 2px; }
  .use-list--left { left: 22px; top: 66px; }
  .use-list--right { left: 138px; top: 66px; }
  .use-box__note { position: absolute; left: 21px; top: 169px; font-size: 13px; line-height: 17px; }

  .flush-claim { position: absolute; left: 72px; top: 408px; width: 271px; height: 78px; }
  .flush-claim svg { position: absolute; left: 0; top: 0; }
  .flush-claim__text { position: absolute; font-family: "Oswald", sans-serif; font-weight: 700; white-space: nowrap; }
  .flush-claim__pct { left: 0; top: -10px; font-size: 46px; letter-spacing: -1px; }
  .flush-claim__line1 { left: 112px; top: 6px; font-size: 27px; }
  .flush-claim__line2 { left: 8px; top: 36px; font-size: 27px; letter-spacing: 0.3px; }

  .directions { position: absolute; left: 67px; top: 511px; width: 300px; font-size: 16.5px; line-height: 20.5px; }
  .directions p + p { margin-top: 19px; }
</style>
</head>
<body>
<div class="canvas">

  <section class="pack pack--front" aria-label="Front of wipe packet">
    <div class="seal seal--top"><div class="seal__band"></div></div>
    <div class="label-panel">
      <svg width="265" height="334" viewBox="0 0 265 334" aria-hidden="true">
        <path d="M0 0 H265 V316 C215 336 165 336 120 324 C75 312 35 302 0 314 Z" fill="#ffffff"/>
      </svg>
    </div>
    <div class="brand-name">roam<br>fresh</div>
    <div class="product-name">Flushable wipe</div>

    <div class="benefit benefit--formula">
      <div class="benefit__icon">
        <svg width="56" height="50" viewBox="0 0 56 50" aria-hidden="true">
          <ellipse cx="28" cy="38" rx="26" ry="7" fill="none" stroke="var(--icon-line)" stroke-width="2"/>
          <ellipse cx="28" cy="36" rx="14" ry="4" fill="none" stroke="var(--icon-line)" stroke-width="2"/>
          <path d="M28 4 C22 14 19 20 19 25 A9 9 0 0 0 37 25 C37 20 34 14 28 4 Z" fill="var(--icon-fill)" stroke="var(--icon-line)" stroke-width="2"/>
        </svg>
      </div>
      <div class="benefit__text">Gentle<br>Cleansing<br>Formula</div>
    </div>

    <div class="benefit benefit--fibers">
      <div class="benefit__icon">
        <svg width="56" height="50" viewBox="0 0 56 50" aria-hidden="true">
          <path d="M28 46 C16 40 14 28 28 4 C42 28 40 40 28 46 Z" fill="var(--icon-fill)" stroke="var(--icon-line)" stroke-width="2"/>
          <path d="M28 46 C16 46 6 38 4 26 C14 26 24 32 28 46 Z" fill="none" stroke="var(--icon-line)" stroke-width="2"/>
          <path d="M28 46 C40 46 50 38 52 26 C42 26 32 32 28 46 Z" fill="none" stroke="var(--icon-line)" stroke-width="2"/>
        </svg>
      </div>
      <div class="benefit__text">100%<br>Natural<br>Fibers</div>
    </div>

    <div class="benefit benefit--free">
      <div class="benefit__icon">
        <svg width="56" height="50" viewBox="0 0 56 50" role="img" aria-label="Feather resting over an open hand">
          <ellipse cx="28" cy="25" rx="22" ry="18" fill="var(--icon-fill)"/>
        </svg>
      </div>
      <div class="benefit__text">No Parabens<br>or Fragrances</div>
    </div>

    <div class="seal seal--bottom"><div class="seal__band"></div></div>
  </section>

  <section class="pack pack--back" aria-label="Back of wipe packet">
    <div class="use-box">
      <div class="use-box__title">FOR USE ON:</div>
      <ul class="use-list use-list--left">
        <li style="top:0"><svg width="16" height="16" viewBox="0 0 16 16" aria-hidden="true"><rect x="1" y="3" width="12" height="12" fill="none" stroke="#fff" stroke-width="1.6"/><path d="M4 8 L7 11 L15 1" fill="none" stroke="#fff" stroke-width="1.8"/></svg>HANDS</li>
        <li style="top:33px"><svg width="16" height="16" viewBox="0 0 16 16" aria-hidden="true"><rect x="1" y="3" width="12" height="12" fill="none" stroke="#fff" stroke-width="1.6"/><path d="M4 8 L7 11 L15 1" fill="none" stroke="#fff" stroke-width="1.8"/></svg>FACE*</li>
        <li style="top:66px"><svg width="16" height="16" viewBox="0 0 16 16" aria-hidden="true"><rect x="1" y="3" width="12" height="12" fill="none" stroke="#fff" stroke-width="1.6"/><path d="M4 8 L7 11 L15 1" fill="none" stroke="#fff" stroke-width="1.8"/></svg>BODY</li>
      </ul>
      <ul class="use-list use-list--right">
        <li style="top:0"><svg width="16" height="16" viewBox="0 0 16 16" aria-hidden="true"><rect x="1" y="3" width="12" height="12" fill="none" stroke="#fff" stroke-width="1.6"/><path d="M4 8 L7 11 L15 1" fill="none" stroke="#fff" stroke-width="1.8"/></svg>NETHER<br>AREAS</li>
        <li style="top:48px"><svg width="16" height="16" viewBox="0 0 16 16" aria-hidden="true"><rect x="1" y="3" width="12" height="12" fill="none" stroke="#fff" stroke-width="1.6"/><path d="M4 8 L7 11 L15 1" fill="none" stroke="#fff" stroke-width="1.8"/></svg>MESSY<br>SURFACES</li>
      </ul>
      <p class="use-box__note">*Avoid eyes/forehead before<br>sweating and scruff (snags fibers)</p>
    </div>

    <div class="flush-claim">
      <svg width="272" height="80" viewBox="0 0 272 80" aria-hidden="true">
        <path d="M112 1 H262 A8 8 0 0 1 270 9 V70 A8 8 0 0 1 262 78 H22" fill="none" stroke="var(--box-line)" stroke-width="1.5"/>
      </svg>
      <span class="flush-claim__text flush-claim__pct">100%</span>
      <span class="flush-claim__text flush-claim__line1">FLUSHABLE</span>
      <span class="flush-claim__text flush-claim__line2">&amp; BIODEGRADABLE</span>
    </div>

    <div class="directions">
      <p>DIRECTIONS: Tear open, unfold wipe, use and flush.</p>
      <p>Please care for our planet, cities, and sewer systems by recycling this packaging after use. Do not flush packaging.</p>
    </div>
  </section>

</div>
</body>
</html>
```